Property lawyer needs a website for new law firm Sydney

WHO AM I ?
I am a real estate development lawyer based in suburban Sydney Australia with over 14 years experience and have recently started my own law firm "Tallowbrook Legal". The firm is just me (a female) at this stage. I need a website designed that is capable of being edited by me frequently (hoping this is easily done?!) and can be published with the domain name I own - www.tallowbrooklegal.com.au.
My areas of practice are:
* Property development (strata & community titling, due diligence, easements, by-laws and management statements, structuring etc)
* Conveyancing (sale and purchase of residential, commercial and retail property)
* General property law (caveats, transfers, related party transactions, easements, leases, powers of attorney etc).
WEBSITE REQUIREMENTS
I would like a website which conveys professionalism, has a fresh modern corporate look and is easy to navigate. The website will mostly be accessed by potential clients looking for information about me, my areas of practice and how to get in contact with me. My potential clients are corporate developers and individuals who are buying and selling property.
My logo for Tallowbrook Legal (see attached) is simple, clean and professional looking. I would like the website to work with the logo without being too dark.
I haven't written all of the content yet, so please use filler text for everything and structure the menus as described above. The site will need to be capable of being updated and edited by me.
Other than that I will leave the design up to you.
Thanks and happy designing!
Target Market(s)
Professional developers and individuals buying and selling real estate
Industry/Entity Type
Real Estate
Coding
Coded - Design and coding required
Number of Pages Required
4 page
Requirements
Must have
- I would like a website which conveys professionalism, has a fresh modern corporate look and is easy to navigate. The website will mostly be accessed by potential clients looking for information about me, my areas of practice and how to get in contact with me. My potential clients are corporate developers and individuals who are buying and selling property.
- Please use my logo for Tallowbrook Legal. I would like the website to work with the logo - the colours are a dark blue (C 100% M 50% B 50%) and grey (C10% B 40%). I don't want the website to be too dark though.
- I am thinking 4 pages. I would like links across the top of the page for "Practice Areas", "About us" and "Contact us" - these should lead to separate landing pages with the content to be inserted later.
- The contact page should contain space for a potential client to send an email enquiry to the following email address "enquiries@tallowbrooklegal.com.au". My contact details are set out in the attached letterhead (see attached).
- I would also like the home page to set out what my three Practice Areas are - Property Development; Conveyancing; General Property Law. Each area should have some filler text under it which will be completed later and a link to be able to take me to the "Practice Areas" page where more detail on each will be provided.
- Please select images that are relevant to my practice as a property lawyer. The photos you use will be the ones which I use so please choose wisely.
- I will need a link on the bottom of the home page showing that I am a member of "The Counsel Guild of NSW" (see attached logo).
- The bottom of each page should also include the following statement "Tallowbrook Legal is a business name of Tallowbrook Legal Pty Limited ACN 482 517 306, an incorporated legal practice regulated by the Legal Profession Act 2004. Liability limited by a scheme approved under the Professional Standards Legislation."
Nice to have
- Have attached an image of me (not the best) but at least its me. Consider whether to use on "About us" page
Should not have
- No images of gavels, scales of justice or law books.
- Images not to be too masculine
- Website not to be too dark

```html
<!DOCTYPE html>
<html lang="en">
<head>
<meta charset="utf-8">
<title>Tallowbrook Legal – Property Lawyers Sydney</title>
<link rel="stylesheet" href="https://fonts.googleapis.com/css2?family=Lora:wght@400;500&family=Arimo:wght@400;700&display=swap">
<style>
:root{
  --navy:#0d3f73;
  --brand-blue:#0f5a98;
  --hex-blue:#3596dc;
  --band:#00467f;
  --page:#e8e8e9;
  --white:#ffffff;
  --text:#555a60;
  --heading:#133f6b;
  --link:#5a8fc4;
  --hero-top:#c9c3c1;
  --hero-bottom:#aeaaa9;
  --photo-top:#dcdde0;
  --photo-bottom:#c6c8cc;
}
*{box-sizing:border-box;margin:0;padding:0}
html,body{width:1171px;height:1200px;overflow:hidden}
body{position:relative;background:var(--page);font-family:"Arimo",Arial,sans-serif;color:var(--text)}
.site-header{position:absolute;left:0;top:0;width:1171px;height:57px;background:var(--white)}
.brand{position:absolute;left:165px;top:12px;font-family:"Lora",serif;font-size:21px;font-weight:400;letter-spacing:0.5px;color:var(--navy);text-transform:uppercase}
.main-nav{position:absolute;right:77px;top:18px;display:flex;gap:31px}
.main-nav a{font-size:12px;font-weight:700;color:#1e2328;text-decoration:none}
.main-nav a.is-active{color:var(--brand-blue)}
.hero{position:absolute;left:0;top:57px;width:1171px;height:369px;background:linear-gradient(180deg,var(--hero-top) 0%,var(--hero-bottom) 100%)}
.hero-band{position:absolute;left:0;top:426px;width:1171px;height:12px;background:var(--band)}
.section-title{position:absolute;left:0;width:1171px;text-align:center;font-family:"Lora",serif;font-weight:400;font-size:26px;color:var(--heading)}
.practice-title{top:457px}
.practice{position:absolute;top:509px;width:195px}
.practice svg{position:absolute;left:12px;top:0}
.practice-label{position:absolute;left:0;top:74px;width:195px;height:47px;background:rgba(205,208,213,0.88);color:var(--heading);font-size:16.5px;line-height:47px;text-align:center;white-space:nowrap}
.practice-link{position:absolute;left:0;top:127px;width:195px;text-align:center;font-size:11px;color:var(--white);text-decoration:underline}
.practice-text{position:absolute;top:213px;width:195px;font-size:10.5px;line-height:14.8px;color:var(--text)}
.contact-title{top:855px}
.call{position:absolute;left:0;top:912px;width:1171px;text-align:center;font-size:18px;color:#4a4d52}
.contact-photo{position:absolute;left:292px;top:955px;width:236px;height:104px;border:5px solid var(--brand-blue);background:linear-gradient(180deg,var(--photo-top) 0%,var(--photo-bottom) 100%)}
.contact-copy{position:absolute;left:547px;top:956px;width:286px;font-size:10px;line-height:11px;color:var(--text)}
.contact-detail{position:absolute;left:547px;font-size:11px;font-weight:700;color:var(--navy)}
.contact-link{position:absolute;left:735px;top:1044px;font-size:10px;color:var(--link);text-decoration:underline}
.site-footer{position:absolute;left:0;top:1137px;width:1171px;height:63px;background:var(--white)}
.footer-brand{position:absolute;left:73px;top:22px;font-family:"Lora",serif;font-size:14px;color:var(--navy);text-transform:uppercase}
.footer-notice{position:absolute;left:294px;top:0;width:586px;height:63px;background:var(--brand-blue);color:var(--white);font-size:7.4px;line-height:11px;text-align:center;padding:17px 10px 0}
.member-badge{position:absolute;left:993px;top:17px;width:36px;height:36px;background:#2a2c30;border-radius:3px}
</style>
</head>
<body>
<header class="site-header">
  <div class="brand">Tallowbrook Legal</div>
  <nav class="main-nav">
    <a href="#" class="is-active">Home</a>
    <a href="#">Practice Areas</a>
    <a href="#">About Us</a>
    <a href="#">Contact Us</a>
  </nav>
</header>

<div class="hero" role="img" aria-label="Photo of cupped hands holding a small model house"></div>
<div class="hero-band"></div>

<h2 class="section-title practice-title">Practice Areas</h2>

<div class="practice" style="left:291px">
  <svg width="170" height="195" viewBox="0 0 170 195" aria-hidden="true"><polygon points="85,0 170,48 170,147 85,195 0,147 0,48" fill="var(--hex-blue)"/></svg>
  <div class="practice-label">Property Developement</div>
  <a class="practice-link" href="#">Learn More</a>
  <p class="practice-text" style="left:-1px">Lorem ipsum dolor sit amet, consectetur adipiscing elit. Fusce accumsan volutpat venenatis. Suspendisse tincidunt dictum massa quis ullamcorper. Nulla quis est nec orci porttitor dignissim.</p>
</div>

<div class="practice" style="left:488px">
  <svg width="170" height="195" viewBox="0 0 170 195" aria-hidden="true"><polygon points="85,0 170,48 170,147 85,195 0,147 0,48" fill="var(--hex-blue)"/></svg>
  <div class="practice-label">Conveyancing</div>
  <a class="practice-link" href="#" style="top:129px">Learn More</a>
  <p class="practice-text" style="left:10px">Lorem ipsum dolor sit amet, consectetur adipiscing elit. Fusce accumsan volutpat venenatis. Suspendisse tincidunt dictum massa quis ullamcorper. Nulla quis est nec orci porttitor dignissim. Suspendisse leo enim, maximus sit amet fermentum ut, dapibus sed elit. Cras sed finibus magna.</p>
</div>

<div class="practice" style="left:685px">
  <svg width="170" height="195" viewBox="0 0 170 195" aria-hidden="true"><polygon points="85,0 170,48 170,147 85,195 0,147 0,48" fill="var(--hex-blue)"/></svg>
  <div class="practice-label">General Property Laws</div>
  <a class="practice-link" href="#">Learn More</a>
  <p class="practice-text" style="left:11px">Nulla facilisi. Ut vel est vel diam laoreet fringilla. Quisque eros nunc, vulputate at felis nec, rhoncus tempus quam. Phasellus rhoncus nibh et venenatis venenatis. Quisque nunc dui, pretium in elementum et, hendrerit vitae mauris.</p>
</div>

<h2 class="section-title contact-title">Contact Us</h2>
<p class="call">Call (###) ###-####</p>

<div class="contact-photo" role="img" aria-label="Photo of a model house resting on architectural plans"></div>
<p class="contact-copy">Nulla facilisi. Ut vel est vel diam laoreet fringilla. Quisque eros nunc, vulputate at felis nec, rhoncus tempus quam. Phasellus rhoncus nibh et venenatis venenatis. Quisque nunc dui, pretium in elementum et, hendrerit vitae mauris.</p>
<p class="contact-detail" style="top:1006px">Phone Number</p>
<p class="contact-detail" style="top:1026px">Email Address</p>
<a class="contact-link" href="#">Visit our Contact Page</a>

<footer class="site-footer">
  <div class="footer-brand">Tallowbrook Legal</div>
  <p class="footer-notice">Tallowbrook Legal is a business name of Tallowbrook Legal Pty Limited ACN 482 517 306, an incorporated legal practice regulated by the Legal Profession Act 2004. Liability limited by a scheme approved under the Professional Standards Legislation.”</p>
  <a href="#" class="member-badge" aria-label="Member of The Counsel Guild of NSW"></a>
</footer>
</body>
</html>
```